Business Card & Email Signature Design || Upmarket + Luxury

Riverlume Honey, a New Zealand Manuka Honey company needs a Business Card & Email Signature design.

Our logo's are attached in Gold & Black versions, feel free to be creative with how you use the logo and it's patterns in your design.

Style:
- Looking for an Elegant, Luxurious, Upmarket feel.
- Black/Matte Black Card, Gold Foil, UV Embossing

Information to Add:

- Logo
- Company Name: Riverlume Honey
- Name: Mattias Brovell
- Title: Creative Director
- Phone: +64 2919 58 617
- Email: mattias@riverlumehoney.example
- Website: www.riverlumehoney.example

- Socials: ***For email Signature Only***
- Facebook: https://www.facebook.com/riverlumehoney/
- Instagram: https://www.instagram.com/riverlumehoney/

Target Market(s)

Asia/Europe Luxury, Upmarket

Contact Information for Business Card

- Logo
- Name: Mattias Brovell
- Phone: +64 2919 58 617

Font styles to use
Other font styles liked:
• Champagne & Limousines (Attached)

Requirements
Must have
• Business Card & Email Signature Design.

Looking for a Sleek, Luxury, Upmarket Design.

```html
<!DOCTYPE html>
<html lang="en">
<head>
<meta charset="utf-8">
<title>Riverlume Honey — Business Card</title>
<link rel="stylesheet" href="https://fonts.googleapis.com/css2?family=Montserrat:wght@400;600&display=swap">
<style>
  :root {
    --stage: #e9e6e0;
    --card: #1d1d1d;
    --gold: #cfb57c;
    --gold-soft: #bfa56f;
    --emboss-top: #3a3a3a;
    --accent-gold: #6b5a24;
    --accent-green: #2f5a2a;
    --accent-blue: #1f4f78;
    --accent-violet: #4a2c6e;
  }
  * { margin: 0; padding: 0; box-sizing: border-box; }
  html, body {
    width: 1200px; height: 782px; overflow: hidden;
    background: var(--stage);
    font-family: "Montserrat", sans-serif;
  }
  .card {
    position: absolute; left: 40px; top: 121px;
    width: 1120px; height: 540px;
    background: var(--card);
    overflow: hidden;
  }
  .emblem-area {
    position: absolute; left: 680px; top: 32px;
    width: 440px; height: 490px;
    border-radius: 48% 0 0 48% / 50% 0 0 50%;
    background:
      radial-gradient(ellipse 22% 10% at 63% 10%, var(--accent-gold) 0%, transparent 100%),
      radial-gradient(ellipse 24% 9% at 66% 36%, var(--accent-green) 0%, transparent 100%),
      radial-gradient(ellipse 28% 11% at 66% 50%, var(--accent-blue) 0%, transparent 100%),
      radial-gradient(ellipse 22% 10% at 66% 63%, var(--accent-violet) 0%, transparent 100%),
      radial-gradient(ellipse 55% 50% at 65% 45%, var(--emboss-top) 0%, var(--card) 100%);
  }
  .person-name {
    position: absolute; left: 241px; top: 78px;
    font-size: 41px; font-weight: 600; letter-spacing: 0.5px;
    color: var(--gold);
  }
  .person-title {
    position: absolute; left: 244px; top: 132px;
    font-size: 22px; font-weight: 400; letter-spacing: 0.5px;
    color: var(--gold-soft);
  }
  .contact-list {
    position: absolute; left: 250px; top: 199px;
    list-style: none;
    font-size: 22px; color: var(--gold-soft); letter-spacing: 0.3px;
  }
  .contact-list li {
    display: flex; align-items: center;
    height: 32px;
  }
  .contact-icon {
    width: 18px; height: 18px; margin-right: 17px; flex: none;
    fill: var(--gold-soft);
  }
  .contact-icon.line { fill: none; stroke: var(--gold-soft); stroke-width: 2; }
  .social-dot {
    width: 17px; height: 17px; border-radius: 50%;
    background: var(--gold-soft);
    margin-right: 17px; flex: none;
  }
  .social-dot.second { margin-left: 14px; margin-right: 10px; }
  .brand {
    position: absolute; left: 84px; top: 370px;
    display: flex; align-items: center;
  }
  .brand-mark {
    width: 64px; height: 64px; border-radius: 50%;
    border: 2px solid var(--gold);
    margin-right: 54px;
  }
  .brand-name {
    font-size: 40px; font-weight: 400; letter-spacing: 5px;
    color: var(--gold); text-transform: uppercase;
  }
</style>
</head>
<body>
  <main class="card">
    <div class="emblem-area" role="img" aria-label="Large embossed brand emblem in matte black with gold, green, blue and violet accents"></div>

    <h1 class="person-name">MATTIAS BROVELL</h1>
    <p class="person-title">Creative Director</p>

    <ul class="contact-list">
      <li>
        <svg class="contact-icon" viewBox="0 0 24 24" aria-hidden="true"><path d="M6.6 10.8a15.1 15.1 0 0 0 6.6 6.6l2.2-2.2a1 1 0 0 1 1-.25 11.4 11.4 0 0 0 3.6.57 1 1 0 0 1 1 1V20a1 1 0 0 1-1 1A17 17 0 0 1 3 4a1 1 0 0 1 1-1h3.5a1 1 0 0 1 1 1c0 1.25.2 2.45.57 3.6a1 1 0 0 1-.25 1z"/></svg>
        +64 2919 58 617
      </li>
      <li>
        <svg class="contact-icon" viewBox="0 0 24 24" aria-hidden="true"><path d="M3 5h18v14H3z M4 6.5v1l8 5 8-5v-1z" fill-rule="evenodd"/></svg>
        mattias@riverlumehoney.example
      </li>
      <li>
        <svg class="contact-icon line" viewBox="0 0 24 24" aria-hidden="true"><circle cx="12" cy="12" r="9"/><ellipse cx="12" cy="12" rx="4" ry="9"/><path d="M3 12h18M5 7h14M5 17h14"/></svg>
        www.riverlumehoney.example
      </li>
      <li>
        <span class="social-dot"></span>/riverlumehoney
        <span class="social-dot second"></span>@riverlumehoney
      </li>
    </ul>

    <div class="brand">
      <span class="brand-mark"></span>
      <span class="brand-name">Riverlume Honey</span>
    </div>
  </main>
</body>
</html>
```